It's a new electrical company based in Newcastle NSW. I would like a logo between the two words "BRANO (insert logo) VOLT". I would like the logo to represent electrical and celtic style. For example I have seen a light bulb with a celtic pattern in the middle which looked very good. I would like it to be a white card, mainly black writing and quite basic not too much going on. But maybe have the logo partially red or green?

Reason: Waiting for new e mail address so I can put it on the business card

Industry/Entity Type

Electrical

Contact Information for Business Card

BRANO VOLT
Electrical Contractors
Domestic, commercial, fault finding, testing, re wires, switchboard upgrades
License No: 730482K
Fully Insured
Phone: 0487310294

```html
<!DOCTYPE html>
<html lang="en">
<head>
<meta charset="utf-8">
<title>Brano Volt – Business Card</title>
<link rel="stylesheet" href="https://fonts.googleapis.com/css2?family=Uncial+Antiqua&family=Open+Sans:wght@400;600&display=swap">
<style>
  :root {
    --page-bg: #e9e6e1;
    --card-bg: #fbfbfa;
    --ink: #1e1e1e;
    --accent-red: #e0201c;
    --band-dark: #2a2a2a;
    --band-mid: #8c8c8c;
    --card-shadow: rgba(0, 0, 0, 0.22);
  }
  * { margin: 0; padding: 0; box-sizing: border-box; }
  html, body {
    width: 1200px;
    height: 1023px;
    overflow: hidden;
    background: var(--page-bg);
  }
  .stage {
    width: 1200px;
    height: 1023px;
    display: flex;
    align-items: center;
    justify-content: center;
  }
  .business-card {
    position: relative;
    width: 920px;
    height: 520px;
    background: var(--card-bg);
    box-shadow: 0 18px 40px var(--card-shadow);
    color: var(--ink);
  }
  .brand {
    position: absolute;
    top: 62px;
    left: 0;
    right: 0;
    display: flex;
    align-items: center;
    justify-content: center;
    gap: 34px;
    font-family: "Uncial Antiqua", serif;
    font-size: 84px;
    letter-spacing: 10px;
    line-height: 1;
    color: var(--ink);
  }
  .brand-dot {
    width: 96px;
    height: 96px;
    border-radius: 50%;
    background: var(--accent-red);
    flex: none;
  }
  .services {
    position: absolute;
    top: 190px;
    left: 0;
    right: 0;
    text-align: center;
    font-family: "Uncial Antiqua", serif;
    font-size: 22px;
    line-height: 1.3;
    letter-spacing: 1.5px;
    color: var(--ink);
  }
  .braid-band {
    position: absolute;
    top: 318px;
    left: 0;
    right: 0;
    height: 34px;
    background: linear-gradient(to bottom, var(--band-dark) 0 4px, var(--band-mid) 4px 30px, var(--band-dark) 30px);
  }
  .contact-block {
    position: absolute;
    top: 402px;
    left: 66px;
    right: 66px;
    display: flex;
    justify-content: space-between;
    font-family: "Open Sans", sans-serif;
  }
  .person-name {
    font-size: 30px;
    font-weight: 600;
    color: var(--accent-red);
    line-height: 1.2;
  }
  .person-role {
    font-size: 22px;
    color: var(--ink);
    margin-top: 4px;
  }
  .contact-details {
    font-size: 22px;
    line-height: 1.35;
    color: var(--ink);
    padding-right: 20px;
  }
  .phone-line {
    display: flex;
    align-items: center;
    gap: 8px;
  }
  .phone-icon { width: 20px; height: 20px; flex: none; }
</style>
</head>
<body>
<main class="stage">
  <article class="business-card">
    <h1 class="brand"><span>BRANO</span><span class="brand-dot" aria-hidden="true"></span><span>VOLT</span></h1>
    <p class="services">Electrical Contractors Domestic,<br>Commercial, Fault Finding, Testing,<br>Rewires, Switchboard upgrades</p>
    <div class="braid-band" role="img" aria-label="Celtic knotwork braid band"></div>
    <div class="contact-block">
      <div class="person">
        <p class="person-name">Electrician Name</p>
        <p class="person-role">Certified Electrician</p>
      </div>
      <div class="contact-details">
        <p class="phone-line">
          <svg class="phone-icon" viewBox="0 0 20 20" aria-hidden="true">
            <circle cx="10" cy="10" r="10" fill="var(--accent-red)"/>
            <path d="M7 5.2c.4-.3.9-.2 1.1.2l.9 1.7c.2.4.1.8-.2 1.1l-.6.5c.5 1.1 1.3 2 2.4 2.6l.6-.5c.3-.3.8-.3 1.1-.1l1.6 1c.4.2.5.7.2 1.1l-.7.9c-.4.5-1.1.7-1.7.5C9.3 13.4 6.6 10.7 5.8 8.2c-.2-.6 0-1.3.5-1.7z" fill="#fff"/>
          </svg>
          0487 310294
        </p>
        <p class="license">License No:730482K</p>
      </div>
    </div>
  </article>
</main>
</body>
</html>
```